WordPress Site Design and Code for Technology Consulting Startup

We need a WordPress design and code to a new site on Nimbo Vault. We have the logo and colors ready. The site will be a brochure site with a CONTACT page that contains a form that the prospective client fills out. The other pages would be ABOUT / SERVICES (3 option drop-down) / SUPPORT. The site should be appropriate for an IT Consulting / IT Managed Services / IT Project Management services in the Chicago area.

Target Market(s)

Across small, medium, large businesses.

Industry/Entity Type

Technology, network infrastructure, IT.

Coding

Coded - Design and coding required

Number of Pages Required

5+ page

Requirements
Nice to have
• I prefer mid-modern / simple / art deco / minimalist.

```html
<!DOCTYPE html>
<html lang="en">
<head>
<meta charset="utf-8">
<title>Corvane – IT Consulting Services</title>
<link href="https://fonts.googleapis.com/css2?family=Michroma&family=Syncopate:wght@700&family=Montserrat:wght@400;500;600;700&display=swap" rel="stylesheet">
<style>
:root{
  --teal:#0894ad;
  --orange:#fb7a16;
  --grey:#c3c3c3;
  --ink:#222;
  --body:#333;
  --line:#d4d4d4;
}
*{box-sizing:border-box;margin:0;padding:0}
html,body{width:1200px;height:3157px;overflow:hidden}
body{position:relative;background:#fff;font-family:'Montserrat',sans-serif;color:var(--body)}
.abs{position:absolute}
.display{font-family:'Syncopate',sans-serif;font-weight:700;text-transform:uppercase}
.brand{font-family:'Syncopate',sans-serif;font-weight:700;color:var(--teal);font-size:25px;letter-spacing:1px}
.nav a{position:absolute;font-family:'Michroma',sans-serif;font-size:12.5px;color:var(--ink);text-decoration:none;letter-spacing:.5px}
.nav a.active{color:var(--orange)}
.nav a.active::after{content:"";position:absolute;left:0;right:0;bottom:-7px;height:2px;background:var(--orange)}
.btn{position:absolute;display:flex;align-items:center;justify-content:center;font-family:'Michroma',sans-serif;font-size:12px;color:#fff;text-transform:uppercase;letter-spacing:.5px;outline:2px solid;outline-offset:-5px}
.btn-teal{background:var(--teal);outline-color:#fff;border:2px solid var(--teal)}
.btn-orange{background:var(--orange);outline-color:#fff;border:2px solid var(--orange)}
.btn-grey{background:var(--grey);outline-color:#fff;border:2px solid var(--grey)}
.hero{left:0;top:94px;width:1200px;height:504px;background:linear-gradient(100deg,#5d6a72 0%,#8a8d8c 30%,#6f6a66 55%,#3a3d44 75%,#6c7378 100%)}
.hero-shade{position:absolute;inset:0;background:rgba(0,0,0,.28)}
.hero h1{position:absolute;left:0;width:1200px;top:166px;text-align:center;color:#fff;font-size:40px;line-height:56px}
.dot{position:absolute;width:14px;height:14px;border:2px solid #fff;border-radius:50%;top:473px}
.dot.on{border-color:var(--orange)}
.dot.on::after{content:"";position:absolute;left:3px;top:3px;width:4px;height:4px;border-radius:50%;background:var(--orange)}
.section-title{color:var(--teal);font-size:29px;line-height:40px}
.rule{position:absolute;height:2px;background:var(--teal)}
.about-text{left:599px;top:672px;width:502px;font-size:13.6px;line-height:20.8px;color:var(--body)}
.about-text p+p{margin-top:20.8px}
.band{left:0;top:1147px;width:1200px;height:1123px;background:var(--teal)}
.svc-title{font-weight:700;font-size:24px;color:#fff;text-transform:uppercase}
.svc-text{font-size:13px;line-height:19.5px;color:#fff;width:400px}
.right{text-align:right}
.field{position:absolute;border:1px solid var(--line);height:38px;display:flex;align-items:center;padding-left:16px;font-size:12.5px;color:#9a9a9a;gap:10px}
.field svg{flex:none}
.footer{left:0;top:2761px;width:1200px;height:396px;background:linear-gradient(110deg,#2b3136 0%,#1d2225 50%,#2e3439 100%)}
.contact-bar{left:107px;top:2934px;width:986px;height:81px;background:#fff;font-size:13.5px;color:var(--ink)}
.contact-bar .item{position:absolute;display:flex;align-items:center;gap:12px}
.social{position:absolute;width:22px;height:22px;border-radius:50%;background:#cfcfcf;top:30px}
.social.on{background:var(--orange);width:26px;height:26px;top:28px}
.foot-nav a{position:absolute;top:3053px;font-family:'Michroma',sans-serif;font-size:12.5px;color:#fff;text-decoration:none}
.foot-nav a.active{color:var(--orange)}
.foot-nav a.active::after{content:"";position:absolute;left:0;right:0;bottom:-6px;height:2px;background:var(--orange)}
</style>
</head>
<body>

<header>
  <div class="abs brand" style="left:87px;top:33px">CORVANE</div>
  <nav class="nav">
    <a class="active" href="#" style="left:459px;top:40px">HOME</a>
    <a href="#" style="left:547px;top:40px">ABOUT US</a>
    <a href="#" style="left:672px;top:40px">SERVICES</a>
    <a href="#" style="left:792px;top:40px">CONTACT US</a>
  </nav>
  <a class="btn btn-teal" style="left:940px;top:28px;width:171px;height:40px">Get in touch</a>
</header>

<section class="abs hero" role="img" aria-label="Photo of smiling business colleagues meeting around a table">
  <div class="hero-shade"></div>
  <h1 class="display">IT Consulting<br>Services</h1>
  <a class="btn btn-orange" style="left:529px;top:293px;width:141px;height:36px;font-size:11.5px">Read more</a>
  <span class="dot" style="left:564px"></span>
  <span class="dot on" style="left:592px"></span>
  <span class="dot" style="left:620px"></span>
</section>

<section class="about">
  <h2 class="abs display section-title" style="left:87px;top:668px;width:480px">We are a young<br>management IT<br>consulting</h2>
  <div class="rule" style="left:87px;top:796px;width:88px"></div>
  <div class="abs about-text">
    <p>Lorem Ipsum is simply dummy text of the printing and typesetting industry. Lorem Ipsum has been the industry's standard dummy text ever since the 1500s, when an unknown printer took a galley of type and scrambled it to make a type specimen book.</p>
    <p>It has survived not only five centuries, but also the leap into electronic typesetting, remaining essentially unchanged. It was popularised in the 1960s with the release of transfer sheets containing Lorem Ipsum passages, and more recently with desktop publishing software like early page layout tools including versions of Lorem Ipsum.</p>
  </div>
  <a class="btn btn-teal" style="left:599px;top:909px;width:142px;height:38px">Read more</a>
</section>

<section class="services">
  <h2 class="abs display section-title" style="left:0;width:1200px;top:1018px;text-align:center">Services</h2>
  <div class="rule" style="left:573px;top:1057px;width:55px"></div>
  <div class="abs band"></div>

  <svg class="abs" style="left:168px;top:1123px" width="390" height="368" viewBox="0 0 390 368" role="img" aria-label="Photo of a developer pointing at code on monitors beside a colleague">
    <defs><linearGradient id="g1" x1="0" y1="0" x2="1" y2="1"><stop offset="0" stop-color="#3c4a58"/><stop offset=".55" stop-color="#9a6a5a"/><stop offset="1" stop-color="#c9b8a8"/></linearGradient></defs>
    <polygon points="0,0 390,0 390,213 195,313 0,213" fill="url(#g1)"/>
    <polygon points="44,256 195,332 195,366 44,287" fill="var(--orange)"/>
    <polygon points="346,256 195,332 195,366 346,287" fill="var(--grey)"/>
  </svg>
  <h3 class="abs svc-title" style="left:644px;top:1193px">IT Consulting</h3>
  <p class="abs svc-text" style="left:644px;top:1232px">Lorem Ipsum is simply dummy text of the printing and typesetting industry. Lorem Ipsum has been the industry's standard dummy text ever since the...</p>
  <a class="btn btn-grey" style="left:644px;top:1307px;width:142px;height:38px">Read more</a>

  <svg class="abs" style="left:649px;top:1529px" width="391" height="368" viewBox="0 0 390 368" role="img" aria-label="Photo of three business people talking at a meeting table">
    <defs><linearGradient id="g2" x1="0" y1="0" x2="1" y2="1"><stop offset="0" stop-color="#2f3640"/><stop offset=".5" stop-color="#b89a82"/><stop offset="1" stop-color="#d9cfc6"/></linearGradient></defs>
    <polygon points="0,0 390,0 390,213 195,313 0,213" fill="url(#g2)"/>
    <polygon points="44,256 195,332 195,366 44,287" fill="var(--orange)"/>
    <polygon points="346,256 195,332 195,366 346,287" fill="var(--grey)"/>
  </svg>
  <h3 class="abs svc-title right" style="left:163px;width:400px;top:1606px">IT Managed Services</h3>
  <p class="abs svc-text right" style="left:163px;top:1645px">Lorem Ipsum is simply dummy text of the printing and typesetting industry. Lorem Ipsum has been the industry's standard dummy text ever since the...</p>
  <a class="btn btn-orange" style="left:421px;top:1721px;width:142px;height:38px">Read more</a>

  <svg class="abs" style="left:168px;top:1936px" width="390" height="368" viewBox="0 0 390 368" role="img" aria-label="Photo of a project team discussing plans at a table">
    <polygon points="0,0 390,0 390,213 195,313 0,213" fill="url(#g2)"/>
    <polygon points="44,256 195,332 195,366 44,287" fill="var(--orange)"/>
    <polygon points="346,256 195,332 195,366 346,287" fill="var(--grey)"/>
  </svg>
  <h3 class="abs svc-title" style="left:644px;top:1975px">IT Project Management</h3>
  <p class="abs svc-text" style="left:644px;top:2015px">Lorem Ipsum is simply dummy text of the printing and typesetting industry. Lorem Ipsum has been the industry's standard dummy text ever since the...</p>
  <a class="btn btn-grey" style="left:644px;top:2090px;width:142px;height:38px">Read more</a>
</section>

<section class="contact">
  <h2 class="abs display section-title" style="left:0;width:1200px;top:2340px;text-align:center;font-size:28px">Get in touch</h2>
  <div class="rule" style="left:573px;top:2378px;width:55px"></div>
  <div class="field" style="left:302px;top:2412px;width:290px"><svg width="13" height="13" viewBox="0 0 13 13" fill="none" stroke="#aaa"><circle cx="6.5" cy="4" r="3"/><path d="M1 12.5c0-3 2.5-5 5.5-5s5.5 2 5.5 5"/></svg>First Name</div>
  <div class="field" style="left:608px;top:2412px;width:290px"><svg width="13" height="13" viewBox="0 0 13 13" fill="none" stroke="#aaa"><circle cx="6.5" cy="4" r="3"/><path d="M1 12.5c0-3 2.5-5 5.5-5s5.5 2 5.5 5"/></svg>Last Name</div>
  <div class="field" style="left:302px;top:2462px;width:290px"><svg width="14" height="11" viewBox="0 0 14 11" fill="none" stroke="#aaa"><rect x=".5" y=".5" width="13" height="10"/><path d="M.5 .5l6.5 5 6.5-5"/></svg>Email</div>
  <div class="field" style="left:608px;top:2462px;width:290px"><svg width="10" height="14" viewBox="0 0 10 14" fill="none" stroke="#aaa"><rect x=".5" y=".5" width="9" height="13" rx="1.5"/><path d="M4 11.5h2"/></svg>Phone</div>
  <div class="field" style="left:302px;top:2512px;width:596px;height:97px;align-items:flex-start;padding-top:14px"><svg width="13" height="13" viewBox="0 0 13 13" fill="none" stroke="#aaa"><path d="M.5 .5h12v8l-4 4h-8z"/><path d="M8.5 12.5v-4h4"/></svg>How can we help?</div>
  <a class="btn btn-teal" style="left:546px;top:2642px;width:109px;height:38px">Submit</a>
</section>

<footer class="abs footer" role="img" aria-label="Darkened photo of a business meeting behind the footer">
  <div class="abs brand" style="left:0;width:1200px;text-align:center;top:108px;font-size:30px">CORVANE</div>
</footer>
<div class="abs contact-bar">
  <div class="item" style="left:25px;top:20px">
    <svg width="16" height="22" viewBox="0 0 16 22"><path d="M8 0a8 8 0 0 0-8 8c0 6 8 14 8 14s8-8 8-14a8 8 0 0 0-8-8z" fill="var(--teal)"/><circle cx="8" cy="8" r="3" fill="#fff"/></svg>
    <span style="line-height:20px">412 W. Lakeview Avenue, Suite<br>800N, Chicago IL 60610</span>
  </div>
  <div class="item" style="left:296px;top:31px">
    <svg width="20" height="15" viewBox="0 0 20 15"><rect width="20" height="15" fill="var(--teal)"/><path d="M1 1l9 7 9-7M1 14l6-6M19 14l-6-6" stroke="#fff" stroke-width="1.4" fill="none"/></svg>
    <span>info@corvaneconsult.com</span>
  </div>
  <div class="item" style="left:555px;top:30px">
    <svg width="18" height="18" viewBox="0 0 24 24"><path d="M6.6 10.8a15 15 0 0 0 6.6 6.6l2.2-2.2c.3-.3.7-.4 1-.2 1.1.4 2.3.6 3.6.6.6 0 1 .4 1 1V20c0 .6-.4 1-1 1A17 17 0 0 1 3 4c0-.6.4-1 1-1h3.5c.6 0 1 .4 1 1 0 1.3.2 2.5.6 3.6.1.3 0 .7-.2 1z" fill="var(--teal)"/></svg>
    <span>312-555-0148</span>
  </div>
  <div class="abs" style="left:740px;top:18px;width:1px;height:45px;background:#ddd"></div>
  <span class="social" style="left:800px" aria-label="Social profile"></span>
  <span class="social" style="left:835px" aria-label="Social profile"></span>
  <span class="social on" style="left:870px" aria-label="Social profile"></span>
  <span class="social" style="left:911px" aria-label="Social profile"></span>
</div>
<nav class="foot-nav">
  <a class="active" href="#" style="left:378px">HOME</a>
  <a href="#" style="left:466px">ABOUT US</a>
  <a href="#" style="left:592px">SERVICES</a>
  <a href="#" style="left:712px">CONTACT US</a>
</nav>
<p class="abs" style="left:0;width:1200px;top:3087px;text-align:center;color:#fff;font-size:13px">Copyright © 2023 Corvane Consulting. All Rights Reserved</p>
<svg class="abs" style="left:1046px;top:3074px" width="34" height="34" viewBox="0 0 34 34" fill="none" stroke="#8a9196" stroke-width="1.5"><circle cx="17" cy="17" r="16"/><path d="M17 25V10M11 16l6-6 6 6M11 9h12"/></svg>

</body>
</html>
```